Velmuts release concert (part 2)

Velmuts is a Reggae/Ska band from Oslo , we are releasing our first album called “overgrown” , friday 29th august at a pub called Tarnwells http://www.tarnwells.no
door open starts 21:00
Concert: 22:00
Price : 150kr

i need this to be printed in a3

Great work , could you guys insert the address and phone of the venue : Tarnwells Nedre Kvistveien 4 0462 Oslo Tlf. 937 82 214 Thanks !

```html
<!DOCTYPE html>
<html lang="en">
<head>
<meta charset="utf-8">
<title>Velmuts – Album Launch Party</title>
<link rel="stylesheet" href="https://fonts.googleapis.com/css2?family=Oswald:wght@400;500;700&display=swap">
<style>
  :root {
    --paper: #efe8d6;
    --ink: #141210;
    --photo-light: #cfc8b6;
    --photo-mid: #7d776c;
    --photo-dark: #2a2724;
  }
  * { margin: 0; padding: 0; box-sizing: border-box; }
  html, body { width: 853px; height: 1200px; overflow: hidden; background: var(--paper); }
  .poster {
    position: relative;
    width: 853px;
    height: 1200px;
    overflow: hidden;
    background: var(--paper);
    font-family: "Oswald", "Arial Narrow", sans-serif;
    color: var(--ink);
    text-transform: uppercase;
  }
  .frame {
    position: absolute;
    inset: 14px 14px 14px 14px;
    border: 30px solid var(--ink);
    border-radius: 8px;
    pointer-events: none;
    z-index: 3;
  }
  .headline {
    position: absolute;
    top: 110px;
    left: 0;
    width: 100%;
    text-align: center;
    font-weight: 700;
    font-size: 58px;
    letter-spacing: 2px;
    line-height: 1.1;
    white-space: nowrap;
  }
  .rule {
    position: absolute;
    top: 196px;
    left: 82px;
    right: 82px;
    height: 3px;
    background: var(--ink);
  }
  .details {
    position: absolute;
    top: 210px;
    left: 96px;
    right: 84px;
    height: 112px;
    display: flex;
    gap: 14px;
  }
  .details .col { line-height: 1.2; white-space: nowrap; }
  .details .divider { width: 3px; background: var(--ink); height: 100%; flex: none; }
  .details .lead { font-weight: 700; font-size: 32px; letter-spacing: 0.5px; line-height: 1.15; margin-bottom: 4px; }
  .details .lead .small { font-weight: 500; font-size: 24px; }
  .details .sub { font-weight: 500; font-size: 17px; letter-spacing: 0.5px; }
  .tagline {
    position: absolute;
    top: 346px;
    width: 100%;
    text-align: center;
    font-weight: 700;
    font-size: 30px;
    line-height: 1.2;
    letter-spacing: 1.5px;
  }
  .band-name {
    position: absolute;
    top: 388px;
    width: 100%;
    text-align: center;
    font-weight: 700;
    font-size: 160px;
    line-height: 1;
    text-transform: lowercase;
    letter-spacing: 4px;
  }
  .album {
    position: absolute;
    top: 580px;
    width: 100%;
    text-align: center;
    font-weight: 700;
    font-size: 30px;
    line-height: 1.2;
    letter-spacing: 1.5px;
  }
  .band-photo {
    position: absolute;
    left: 44px;
    right: 44px;
    top: 650px;
    bottom: 44px;
    background: linear-gradient(180deg, var(--paper) 0%, var(--photo-light) 14%, var(--photo-mid) 48%, var(--photo-dark) 100%);
    z-index: 1;
  }
</style>
</head>
<body>
  <main class="poster">
    <div class="band-photo" role="img" aria-label="Black and white photo of the seven band members standing on outdoor concrete steps"></div>

    <h1 class="headline">Album Launch Party</h1>
    <div class="rule"></div>

    <section class="details">
      <div class="col event">
        <div class="lead">Friday 29th August</div>
        <div class="sub">Doors open 21:00 - Concert 22:00</div>
        <div class="sub">Entry 150kr</div>
      </div>
      <div class="divider"></div>
      <div class="col venue">
        <div class="lead">Tarnwells <span class="small">Roots &amp; Blues</span></div>
        <div class="sub">Nedre Kvistveien 4, 0462 Oslo</div>
        <div class="sub">Tel: 937 82 214 &nbsp;www.tarnwells.no</div>
      </div>
    </section>

    <p class="tagline">Oslo Reggae-Ska Band</p>
    <h2 class="band-name">Velmuts</h2>
    <p class="album">Debut album “Overgrown”</p>

    <div class="frame"></div>
  </main>
</body>
</html>
```